Brightmoor Card Company Business Cards

We are a trading card store with Zorblix, sports and other TCG cards, we need a business card design that encompasses a clean cut, modern style with a retro flare. website is brightmoorcardco.com for reference. Can utilize a comic book era feel or a more modern outdoor feel to utilize the "Pacific Northwest" elements of tress, mountains, etc.

Industry/Entity Type

Trading cards and collectibles

Contact Information for Business Card

business name, email address, phone number, name, owner job title

Font styles to use
Sans Serif

```html
<!DOCTYPE html>
<html lang="en">
<head>
<meta charset="utf-8">
<title>Brightmoor Card Company – Business Cards</title>
<link rel="stylesheet" href="https://fonts.googleapis.com/css2?family=Montserrat:wght@400;500;600;700;800&display=swap">
<style>
  :root {
    --stage: #d3d3d3;
    --card-grey: #767676;
    --photo-dark: #3c3c3c;
    --photo-light: #9a9a9a;
    --accent-cyan: #1ebfe0;
    --accent-orange: #ef5b30;
    --ink-light: #ffffff;
  }
  * { box-sizing: border-box; margin: 0; padding: 0; }
  html, body {
    width: 1200px; height: 764px; overflow: hidden;
    background: var(--stage);
    font-family: "Montserrat", sans-serif;
  }
  .stage { position: relative; width: 1200px; height: 764px; }
  .card {
    position: absolute; width: 510px; height: 290px;
    border-radius: 11px; overflow: hidden;
    box-shadow: 3px 5px 8px rgba(0,0,0,0.28);
  }
  .card--front { left: 74px; top: 241px; background: var(--card-grey); }
  .card--back { left: 617px; top: 239px; background: var(--accent-orange); }

  .front-art { position: absolute; inset: 0; width: 510px; height: 290px; }
  .collage { position: absolute; left: 0; top: 0; width: 190px; height: 290px; }

  .brand-mark {
    position: absolute; left: 40px; top: 82px; width: 200px;
    display: flex; align-items: center; gap: 8px;
    color: var(--ink-light); font-weight: 700; font-size: 15px;
    line-height: 1.15; letter-spacing: 0.02em; text-transform: uppercase;
  }
  .brand-mark__dot {
    flex: none; width: 12px; height: 12px; border-radius: 50%;
    background: var(--accent-cyan);
  }

  .contact { position: absolute; left: 284px; top: 0; color: var(--ink-light); }
  .contact__name {
    position: absolute; top: 66px; white-space: nowrap;
    font-weight: 800; font-size: 22px; letter-spacing: -0.02em;
  }
  .contact__title {
    position: absolute; top: 96px; white-space: nowrap;
    font-weight: 400; font-size: 16px;
  }
  .contact__line {
    position: absolute; white-space: nowrap;
    font-weight: 500; font-size: 10px; line-height: 12.5px; text-transform: uppercase;
  }
  .contact__email { top: 144px; }
  .contact__web { top: 170px; }
  .contact__address { top: 194px; }
  .contact__phone { top: 240px; }

  .slogan {
    position: absolute; left: 49px; top: 48px; color: var(--ink-light);
    font-weight: 800; font-size: 40px; line-height: 36px; letter-spacing: -0.03em;
    text-transform: uppercase;
  }
  .tagline {
    position: absolute; left: 49px; top: 129px; color: var(--ink-light);
    font-weight: 400; font-size: 16px;
  }
  .website {
    position: absolute; left: 49px; top: 218px; color: var(--ink-light);
    font-weight: 700; font-size: 19px; letter-spacing: -0.01em;
  }
</style>
</head>
<body>
<main class="stage">
  <section class="card card--front" aria-label="Business card front">
    <svg class="front-art" viewBox="0 0 510 290" aria-hidden="true">
      <defs>
        <linearGradient id="collageTone" x1="0" y1="0" x2="1" y2="1">
          <stop offset="0" stop-color="var(--photo-light)"/>
          <stop offset="0.5" stop-color="#6a6a6a"/>
          <stop offset="1" stop-color="var(--photo-dark)"/>
        </linearGradient>
      </defs>
      <polygon points="190,0 200,0 268,290 258,290" fill="var(--accent-cyan)"/>
      <polygon points="0,0 190,0 258,290 0,290" fill="url(#collageTone)"/>
    </svg>
    <div class="collage" role="img" aria-label="Greyscale collage of sports trading cards"></div>

    <div class="brand-mark">
      <span class="brand-mark__dot"></span>
      <span>Brightmoor<br>Card Company</span>
    </div>

    <div class="contact">
      <p class="contact__name">SAM ELLERY</p>
      <p class="contact__title">DIRECTOR</p>
      <p class="contact__line contact__email">sam@brightmoorcardco.com</p>
      <p class="contact__line contact__web">brightmoorcardco.com</p>
      <p class="contact__line contact__address">418 Harbor Ridge Avenue,<br>Brightmoor, WA<br>98201-4420</p>
      <p class="contact__line contact__phone">+1 (555) 014-2270</p>
    </div>
  </section>

  <section class="card card--back" aria-label="Business card back">
    <h1 class="slogan">Start<br>the hunt</h1>
    <p class="tagline">Trading cards and collectibles</p>
    <p class="website">www.brightmoorcardco.com</p>
  </section>
</main>
</body>
</html>
```